Expanding the consciousness of Humanity - Solvane-Harbor

Please note that whoever will win this project , a 1on1 Powerpoint design project will separately be launched and will be offered to the winning designer.

---------
This letterhead is to provide proposals, as well as manuals for my clients.

I am looking for the letter, power point design and business card that inspires people when they see it, that they feel that design has been done with love and passion. Something that is professional, simple and yet creative, Business like, yet spiritual. That inspires growth!

This part of the branding for my company, therefore the business card as well as the power point design that will come after as 1on1 project should have the same team and feeling.

Solvane harbor, The company will be providing Coaching services (one-one or groups) to corporations, teams and individuals, partnering with them to achieve their goals/vision, by helping them to remove the self-imposed limiting beliefs, helping them to get them out of their own way, helping them to raise their level of consciousness and self-awareness.

The vision is: Bring conscious leadership to the workplace and to individuals for the wellbeing of humanity.

I know that somewhere out there will resonate with this, and will be inspired to provide the best design :) thank you very much!!!!!

MPORTANT:
- To use Free Fonts - let me know where I can download them
- Editable formats please for the double sized business card

LOGO is attached in pdf. If needed other file type please let me know

Thank you thank you in advance for your time and inspiration!! Sending good vibes for a great design out there

Must Have:
- Please keep on mind that the cards - power point will have the same feeling - Corporate branding
- that is not to heavy to look at it, that is simple and beautiful and inspiring
- Looking to have Calibri or Calibri light font

imple, yet inspirational - Professional, yet playful - business like, yet spiritual

I am looking for something different that the "standard" designs out there.

For example, the Logo of the company in the back side with a quote and the front side something simple, yet inspiring. that has the contact info as well as the social media details LinkedIn - Facebook - tweeter - website

Open for suggestions and inspiration :)

Thank you!

Font styles to use
Sans Serif

Requirements
Must have
• - Please keep on mind that the cards - power point will have the same feeling
• - Corporate branding
• - that is not to heavy to look at it, that is simple and beautiful and inspiring
• - Looking to have Calibri or Calibri light font
• - Corporate colours as the logo

```html
<!DOCTYPE html>
<html lang="en">
<head>
<meta charset="utf-8">
<title>Solvane-Harbor Letterhead</title>
<link href="https://fonts.googleapis.com/css2?family=Carlito:wght@400;700&display=swap" rel="stylesheet">
<style>
  :root {
    --brand-yellow: #f7be00;
    --brand-blue: #23407f;
    --paper: #ffffff;
    --backdrop: #d3d4d1;
    --ink-soft: #5a6478;
  }
  * { margin: 0; padding: 0; box-sizing: border-box; }
  html, body {
    width: 1200px; height: 784px; overflow: hidden;
    background: var(--backdrop);
    font-family: "Carlito", Calibri, sans-serif;
  }
  .letterhead {
    position: absolute; left: 320px; top: 30px;
    width: 560px; height: 724px;
    background: var(--paper);
  }
  .corner-bar { position: absolute; height: 6px; }
  .corner-bar--tl-blue { top: 10px; left: 34px; width: 34px; background: var(--brand-blue); }
  .corner-bar--tl-yellow { top: 22px; left: 10px; width: 34px; background: var(--brand-yellow); }
  .corner-bar--tr-blue { top: 10px; right: 10px; width: 34px; background: var(--brand-blue); }
  .corner-bar--tr-yellow { top: 22px; right: 34px; width: 34px; background: var(--brand-yellow); }

  .footer-band { position: absolute; bottom: 0; left: 0; right: 0; height: 10px; display: flex; gap: 4px; }
  .footer-band__yellow { flex: 0 0 74%; background: var(--brand-yellow); }
  .footer-band__blue { flex: 1; background: var(--brand-blue); }

  .brand {
    position: absolute; top: 36px; left: 40px;
    display: flex; align-items: center; gap: 8px;
  }
  .brand__dot {
    width: 36px; height: 36px; border-radius: 50%;
    background: var(--brand-blue);
  }
  .brand__divider { width: 1px; height: 38px; background: var(--brand-blue); }
  .brand__name {
    font-size: 17px; font-weight: 400; letter-spacing: 0.5px;
    color: var(--brand-yellow); text-transform: uppercase; line-height: 1;
  }
  .brand__tagline {
    margin-top: 3px; font-size: 7.5px; letter-spacing: 0.8px;
    color: var(--brand-blue); text-transform: uppercase;
  }

  .contact {
    position: absolute; top: 40px; right: 30px;
    list-style: none; font-size: 8px; line-height: 12px; color: var(--ink-soft);
  }
  .contact__item { display: flex; align-items: flex-start; gap: 5px; }
  .contact__icon { width: 7px; height: 7px; margin-top: 2.5px; flex: 0 0 7px; }
</style>
</head>
<body>
  <main class="letterhead">
    <span class="corner-bar corner-bar--tl-blue"></span>
    <span class="corner-bar corner-bar--tl-yellow"></span>
    <span class="corner-bar corner-bar--tr-blue"></span>
    <span class="corner-bar corner-bar--tr-yellow"></span>

    <header class="brand">
      <span class="brand__dot"></span>
      <span class="brand__divider"></span>
      <div class="brand__text">
        <div class="brand__name">Solvane-Harbor</div>
        <div class="brand__tagline">Clear Minds · Steady Growth</div>
      </div>
    </header>

    <ul class="contact">
      <li class="contact__item">
        <svg class="contact__icon" viewBox="0 0 10 10"><path d="M5 0.5a3.3 3.3 0 0 0-3.3 3.3C1.7 6.3 5 9.5 5 9.5s3.3-3.2 3.3-5.7A3.3 3.3 0 0 0 5 .5z" fill="#23407f"/><circle cx="5" cy="3.8" r="1.2" fill="#fff"/></svg>
        <span>Larkfield Avenue, Suite 210<br>Aldenport 40218</span>
      </li>
      <li class="contact__item">
        <svg class="contact__icon" viewBox="0 0 10 10"><path d="M2 .8l2 2-1 1.3c.7 1.3 1.6 2.2 2.9 2.9L7.2 6l2 2-1.2 1.5C4.5 9.3.7 5.5.5 2z" fill="#23407f"/></svg>
        <span>(555) 014-2280</span>
      </li>
      <li class="contact__item">
        <svg class="contact__icon" viewBox="0 0 10 10"><path d="M2 .8l2 2-1 1.3c.7 1.3 1.6 2.2 2.9 2.9L7.2 6l2 2-1.2 1.5C4.5 9.3.7 5.5.5 2z" fill="#23407f"/></svg>
        <span>(555) 014-2291</span>
      </li>
      <li class="contact__item">
        <svg class="contact__icon" viewBox="0 0 10 10"><rect x=".5" y="2" width="9" height="6.5" fill="#23407f"/><path d="M.8 2.3L5 5.6l4.2-3.3" stroke="#fff" stroke-width=".9" fill="none"/></svg>
        <span>hello@solvaneharbor.com</span>
      </li>
      <li class="contact__item">
        <svg class="contact__icon" viewBox="0 0 10 10"><circle cx="5" cy="5" r="4.3" fill="none" stroke="#23407f" stroke-width="1.2"/><path d="M.8 5h8.4M5 .7c-2.2 2.4-2.2 6.2 0 8.6M5 .7c2.2 2.4 2.2 6.2 0 8.6" stroke="#23407f" stroke-width=".8" fill="none"/></svg>
        <span>www.solvaneharbor.com</span>
      </li>
    </ul>

    <footer class="footer-band">
      <span class="footer-band__yellow"></span>
      <span class="footer-band__blue"></span>
    </footer>
  </main>
</body>
</html>
```